Serviceleitfaden für das Hotel
Zielgruppe
Lindholms Hotel
Hallo,
ich brauch eine Serviceleitfaden in Form eines Flyers
Titelseite:
Logo , darunter den Begriff : Serviceleitfaden
Innenseite 1 Links:
Fernsehprogramme
1. KMT
2. BWX
3. NPQ
4. Dux 1
5. Via Zehner
6. Welle Vier
7. Jul
8. Funk 7
9. NPQ 2
ab 10 die Programme von Orbo
http://business.orbo-tv.de/obs/cms/de/hotel-zimmerloesung-basispaket.jsp
alle Sender außer Orbo 3D
Innenseite 1 Rechts, Innenseite 2 Links und Rechts
Serviceleitfaden
http://www.hotel-lindholms.de/de/zimmer/service-leitfaden
Rückseite:
Telefonnummern
Internet
Sie könne sich kostenlos bei Netzwerkfunkhaus über Wlan anmelden.
Danach müssen Sie nur Ihren Browser öffnen.
Anfahrskizze:
Siehe Bild
Druckformat:
http://www.papierwerk-online.de/tpl/holt-team/media/pdv/druckdatenskizzen/faltblatt__gefalzt_auf_din_a4__6-seiter_%28zickzackfalz%29_2.pdf
http://www.papierwerk-online.de/tpl/holt-team/media/pdv/druckdatenskizzen/faltblatt__gefalzt_auf_din_a4__6-seiter_%28zickzackfalz%29_1.pdf

```html
<!DOCTYPE html>
<html lang="de">
<head>
<meta charset="utf-8">
<title>Lindholms Hotel – Service-Leitfaden</title>
<link href="https://fonts.googleapis.com/css2?family=Jost:wght@400;500;600&display=swap" rel="stylesheet">
<style>
  :root {
    --gold: #9a7d44;
    --ink: #1d1d1b;
    --paper: #ffffff;
    --map-tone: #ede6d8;
  }
  * { margin: 0; padding: 0; box-sizing: border-box; }
  html, body { width: 1200px; height: 848px; overflow: hidden; background: var(--paper); }
  body { position: relative; font-family: "Jost", sans-serif; color: var(--ink); }

  .sheet {
    position: absolute; left: 68px; top: 161px; width: 1067px; height: 503px;
    background: var(--paper); box-shadow: 0 1px 4px rgba(0,0,0,.35);
  }
  .band { position: absolute; left: 0; top: 0; width: 100%; height: 101px; background: var(--gold); }
  .band-title {
    position: absolute; top: 72px; color: #fff; font-weight: 600;
    font-size: 14px; letter-spacing: 1.1px; line-height: 1;
  }
  .band-title.left { left: 106px; }
  .band-title.mid { left: 461px; }

  .brand-mark {
    position: absolute; left: 800px; top: 60px; display: flex; align-items: center; gap: 8px;
    color: #fff; font-weight: 500; font-size: 18px; letter-spacing: 1px;
  }
  .brand-mark .dot { width: 26px; height: 26px; border-radius: 50%; background: #fff; }

  .column { position: absolute; top: 125px; width: 130px; font-size: 6.4px; line-height: 9px; }
  .entry { position: relative; margin-bottom: 9px; }
  .entry h3 { color: var(--gold); font-weight: 600; font-size: 6.8px; letter-spacing: .4px; }
  .entry .letter {
    position: absolute; left: -13px; top: 0; color: var(--gold); font-weight: 600; font-size: 6.8px;
  }
  .entry strong { font-weight: 600; }
  .entry.spaced { margin-top: 18px; }

  .col-a { left: 59px; }
  .col-f { left: 216px; }
  .col-k { left: 414px; }
  .col-t { left: 572px; }

  .contact { position: absolute; left: 768px; top: 198px; width: 150px; font-size: 6.4px; line-height: 9px; }
  .contact h3, .internet h3 { color: var(--gold); font-weight: 600; font-size: 6.8px; }
  .contact .gap { height: 9px; }
  .contact .web { color: var(--gold); font-weight: 600; }
  .internet { position: absolute; left: 926px; top: 198px; width: 115px; font-size: 6.4px; line-height: 9px; }

  .route-map { position: absolute; left: 768px; top: 301px; width: 264px; height: 135px; background: var(--map-tone); }

  .footer-rule { position: absolute; top: 459px; height: 1px; background: var(--gold); }
  .footer-rule.r1 { left: 0; width: 152px; }
  .footer-rule.r2 { left: 250px; width: 257px; }
  .footer-rule.r3 { left: 605px; width: 462px; }
  .footer-mark {
    position: absolute; top: 452px; display: flex; align-items: center; gap: 4px;
    color: var(--gold); font-weight: 500; font-size: 9px; letter-spacing: .4px;
  }
  .footer-mark.m1 { left: 160px; }
  .footer-mark.m2 { left: 515px; }
  .footer-mark .dot { width: 11px; height: 11px; border-radius: 50%; background: var(--ink); }
</style>
</head>
<body>
<div class="sheet">
  <div class="band"></div>
  <h2 class="band-title left">SERVICE-LEITFADEN</h2>
  <h2 class="band-title mid">SERVICE-LEITFADEN</h2>
  <div class="brand-mark"><span>Lindholms Hotel</span><span class="dot"></span></div>

  <div class="column col-a">
    <div class="entry"><span class="letter">A</span><h3>ABREISE</h3>Wir bitten Sie freundlichst,<br>Ihr Zimmer am Abreisetag bis<br>11:00 Uhr zu räumen.</div>
    <div class="entry"><span class="letter">B</span><h3>BABYBETTEN</h3>Babybetten stellen wir bei Bedarf<br>gerne zur Verfügung.</div>
    <div class="entry"><h3>BEZAHLUNG</h3>Bitte begleichen Sie Ihre Rech-<br>nung bei Abreise. Neben der<br>EC-Karte können Sie auch mit<br>Kartell, Amplo oder Vira-<br>Card bezahlen.</div>
    <div class="entry"><h3>BRIEFMARKEN</h3>Postwertzeichen haben wir an<br>der Rezeption vorrätig.</div>
    <div class="entry"><span class="letter">E</span><h3>ELEKTRISCHE ANSCHLÜSSE</h3>In den Zimmern und Bädern sind<br>ausreichend Steckdosen vor-<br>handen. Diese entsprechen der<br>deutschen Norm mit 230V/50Hz.</div>
  </div>

  <div class="column col-f">
    <div class="entry"><span class="letter">F</span><h3>FAHRSTUHL</h3>Der Fahrstuhl des Hotels befindet<br>sich beim Hintereingang.</div>
    <div class="entry"><h3>FRÜHSTÜCK</h3><strong>Montag – Freitag</strong><br>von 6:30 Uhr bis 10:00 Uhr<br><strong>Samstag und Sonntag</strong><br>von 8:00 Uhr bis 10:00 Uhr</div>
    <div class="entry"><span class="letter">G</span><h3>GUTSCHEINE</h3>Gutscheine können an der<br>Rezeption erworben werden.</div>
    <div class="entry"><span class="letter">H</span><h3>HANDTÜCHER</h3>Wenden Sie sich bitte an die<br>Rezeption, wenn Sie weitere<br>Handtücher benötigen.</div>
    <div class="entry"><h3>HAUSTIERE</h3>Haustiere sind im Hotel<br>nicht gestattet.</div>
    <div class="entry"><span class="letter">I</span><h3>INTERNET</h3>Zugangskennungen für die Nut-<br>zung unseres kostenfreies WLAN</div>
  </div>

  <div class="column col-k">
    <div class="entry"><span class="letter">K</span><h3>KREDITKARTEN</h3>Neben der EC-Karte können Sie<br>auch mit Kartell, Amplo,<br>Dinora oder Vira-Card bezahlen.</div>
    <div class="entry"><span class="letter">P</span><h3>PARKPLÄTZE</h3>Stellplätze für Pkw, Motorräder<br>und Busse stehen ausreichend<br>und kostenfrei im Außenbereich<br>des Hotels zur Verfügung. Die<br>Benutzung erfolgt auf eigene<br>Gefahr, für Schäden kann keine<br>Haftung übernommen werden.<br>Der Parkplatz befindet sich in der<br>Sackgasse der Feldstrasse 12.</div>
    <div class="entry"><span class="letter">R</span><h3>RAUCHEN</h3>Das Rauchen ist nicht gestattet.</div>
    <div class="entry"><h3>REZEPTION</h3><strong>Montag – Freitag</strong><br>von 6:30 Uhr bis 12:00 Uhr und<br>von 15:00 Uhr bis 22:00 Uhr<br><strong>Samstag und Sonntag</strong><br>von 8:30 Uhr bis 12:00 Uhr und<br>von 18:00 Uhr bis 21:00 Uhr</div>
  </div>

  <div class="column col-t">
    <div class="entry"><span class="letter">T</span><h3>TELEFON</h3>Alle Zimmer sind mit Selbst-<br>wahltelefonen ausgestattet.<br>Sie können auch ohne Vermitt-<br>lung erreicht werden.<br><br><strong>Amt: 0<br>Zentrale: 10<br>Notruf: 112</strong></div>
    <div class="entry"><span class="letter">W</span><h3>WECKDIENST</h3>Teilen Sie der Rezeption Ihren<br>Wecktermin mit.</div>
    <div class="entry spaced"><span class="letter">Z</span><h3>ZIMMERSCHLÜSSEL</h3>Bitte geben Sie Ihren Zimmer-<br>schlüssel bei Abreise und Be-<br>zahlung ab.</div>
  </div>

  <div class="contact">
    <h3>Lindholms Hotel Halmstede</h3>
    Jonas Lindholm<br>Lindenweg 42<br>27451 Halmstede Deutschland
    <div class="gap"></div>
    Telefon: +49 (0) 4000-12340<br>Telefax: +49 (0) 4000-123450
    <div class="gap"></div>
    <span class="web">www.lindholms-hotel.de</span>
  </div>

  <div class="internet">
    <h3>Internet:</h3>
    Sie könne sich kostenlos bei Netzwerk-<br>funkhaus über Wlan anmelden.<br>Danach müssen Sie nur Ihren Browser<br>öffnen.
  </div>

  <div class="route-map" role="img" aria-label="Anfahrtsskizze: Straßen rund um das Hotel mit markiertem Hotelparkplatz in der Sackgasse"></div>

  <div class="footer-rule r1"></div>
  <div class="footer-mark m1"><span>Lindholms Hotel</span><span class="dot"></span></div>
  <div class="footer-rule r2"></div>
  <div class="footer-mark m2"><span>Lindholms Hotel</span><span class="dot"></span></div>
  <div class="footer-rule r3"></div>
</div>
</body>
</html>
```